Harrowgate Legal

To update and modernize current business card appearance. Marisa's business is based in Melbourne with 4 other lawyers in the firm. Marisa travels to the Pilbara in Western Australia approximately 1 week a month as part of the firms legal work. She consults with clients in Newman, Tom Price and Port Hedland. The lawyers work mostly from a home office, apart from court appearances. They have a virtual office in Melbourne city, and use facilities in 3 or 4 other locations around Melbourne. It is important the client's think this is a conventional law firm with a permanent office. Our business structure is a difficult concept for them to grasp. The business has been operational for 3 years, growing from 1 lawyer to 4 lawyers during that time. Our website is www.Harrowgatelegal.com.au and is currently being upgraded as we are not happy with its content. The logo is currently orange and dark grey but the orange is a difficult colour to reproduce and often turns out "poo" brown when documents are printed. We need clients to know we are user friendly and caring - and not head up our rears ends as some lawyers appear to be.
Updates

Thank you for the feedback so far. 1. Some of the designs have too much black (We prefer darker grey & not too much.) 2. Happy for designers to play around with different colours & logo design. What we're after is a modern look and business card that people say "wow" when they pick it up.

Industry/Entity Type

Business

```html
<!DOCTYPE html>
<html lang="en">
<head>
<meta charset="utf-8">
<title>Harrowgate Legal — Business Card</title>
<link rel="stylesheet" href="https://fonts.googleapis.com/css2?family=Crimson+Text:wght@400;700&family=Open+Sans:wght@400&display=swap">
<style>
  :root {
    --page-bg: #d9dadb;
    --card-white: #ffffff;
    --slate: #58595b;
    --slate-text: #5f6062;
    --claret: #a50d15;
    --ink-light: #ffffff;
    --shadow: rgba(0,0,0,0.18);
  }
  * { margin: 0; padding: 0; box-sizing: border-box; }
  html, body { width: 1200px; height: 1200px; overflow: hidden; }
  body {
    background: var(--page-bg);
    position: relative;
    font-family: "Crimson Text", Georgia, serif;
  }
  .card {
    position: absolute;
    left: 216px;
    width: 764px;
    height: 462px;
    background: var(--card-white);
    box-shadow: 0 1px 4px var(--shadow);
    overflow: hidden;
  }
  .card--front { top: 130px; }
  .card--back { top: 600px; }

  .brand {
    position: absolute;
    left: 0; right: 0;
    top: 22px;
    display: flex;
    flex-direction: column;
    align-items: center;
  }
  .brand__dot {
    width: 86px; height: 86px;
    border-radius: 50%;
    background: var(--claret);
  }
  .brand__name {
    margin-top: 26px;
    font-family: "Crimson Text", Georgia, serif;
    font-weight: 400;
    font-size: 40px;
    letter-spacing: 3px;
    text-transform: uppercase;
    color: var(--slate-text);
    line-height: 1;
  }

  .services {
    position: absolute;
    left: 0; right: 0; bottom: 0;
    height: 204px;
    background: var(--slate);
    color: var(--ink-light);
    text-align: center;
    padding-top: 10px;
  }
  .services__heading { font-weight: 700; font-size: 26px; line-height: 32px; }
  .services__list {
    display: flex; justify-content: center; gap: 24px;
    font-size: 23px; line-height: 30px;
  }
  .services__tagline {
    margin-top: 18px;
    font-size: 16px; letter-spacing: 1.5px; word-spacing: 6px;
  }
  .services__web {
    margin-top: 10px;
    font-weight: 700; font-size: 22px; letter-spacing: 1.6px;
  }

  .contact-band {
    position: absolute;
    left: 0; right: 0; bottom: 0;
    height: 204px;
    background: var(--claret);
    color: var(--ink-light);
  }
  .person { position: absolute; left: 25px; top: 52px; }
  .person__name { font-weight: 700; font-size: 29px; line-height: 34px; }
  .person__creds { font-size: 17px; line-height: 22px; }
  .person__role { font-size: 26px; line-height: 36px; margin-top: 4px; }

  .contacts {
    position: absolute; left: 358px; top: 38px;
    list-style: none;
    font-family: "Open Sans", Arial, sans-serif;
    font-size: 19px;
  }
  .contacts li {
    display: flex; align-items: center; gap: 10px;
    height: 34px;
  }
  .contacts svg { width: 18px; height: 18px; fill: var(--ink-light); flex: none; }
</style>
</head>
<body>

<section class="card card--front">
  <div class="brand">
    <div class="brand__dot"></div>
    <div class="brand__name">Harrowgate Legal</div>
  </div>
  <div class="services">
    <p class="services__heading">Family Law</p>
    <p class="services__list">
      <span>Collaborative Practice</span>
      <span>Mediation &amp; Negotiation</span>
      <span>Intervention Orders</span>
    </p>
    <p class="services__heading">Criminal Law</p>
    <p class="services__tagline">EXPERIENCE SUPPORT SOLUTIONS</p>
    <p class="services__web">www.harrowgatelegal.com.au</p>
  </div>
</section>

<section class="card card--back">
  <div class="brand">
    <div class="brand__dot"></div>
    <div class="brand__name">Harrowgate Legal</div>
  </div>
  <div class="contact-band">
    <div class="person">
      <p class="person__name">J. Marisa Whitlock</p>
      <p class="person__creds">LLB(Hons) - Accredited Mediator</p>
      <p class="person__role">Principal Solicitor</p>
    </div>
    <ul class="contacts">
      <li>
        <svg viewBox="0 0 24 24" aria-hidden="true"><path d="M6.6 10.8a15.1 15.1 0 0 0 6.6 6.6l2.2-2.2c.3-.3.7-.4 1-.2 1.1.4 2.3.6 3.6.6.6 0 1 .4 1 1V20c0 .6-.4 1-1 1A17 17 0 0 1 3 4c0-.6.4-1 1-1h3.5c.6 0 1 .4 1 1 0 1.3.2 2.5.6 3.6.1.3 0 .7-.2 1z"/></svg>
        <span>1300 HARROW (427 769)</span>
      </li>
      <li>
        <svg viewBox="0 0 24 24" aria-hidden="true"><path d="M7 2h10a1 1 0 0 1 1 1v18a1 1 0 0 1-1 1H7a1 1 0 0 1-1-1V3a1 1 0 0 1 1-1zm1 3v11h8V5zm4 13a1 1 0 1 0 0 2 1 1 0 0 0 0-2z"/></svg>
        <span>0412 555 018</span>
      </li>
      <li>
        <svg viewBox="0 0 24 24" aria-hidden="true"><path d="M2 6l10 7 10-7v12H2z M2 5h20l-10 7z"/></svg>
        <span>marisa.whitlock@harrowgatelegal.com.au</span>
      </li>
      <li>
        <svg viewBox="0 0 24 24" aria-hidden="true"><path d="M12 2a10 10 0 1 0 0 20 10 10 0 0 0 0-20zm0 2c.9 0 2.1 1.8 2.7 5H9.3C9.9 5.8 11.1 4 12 4zM9.1 11h5.8a18 18 0 0 1 0 2H9.1a18 18 0 0 1 0-2zM4.1 11h3a20 20 0 0 0 0 2h-3a8 8 0 0 1 0-2zm12.8 0h3a8 8 0 0 1 0 2h-3a20 20 0 0 0 0-2zM9.3 15h5.4c-.6 3.2-1.8 5-2.7 5s-2.1-1.8-2.7-5zM5 9a8 8 0 0 1 4.4-4.3A12 12 0 0 0 7.3 9zm9.6-4.3A8 8 0 0 1 19 9h-2.3a12 12 0 0 0-2.1-4.3zM5 15h2.3a12 12 0 0 0 2.1 4.3A8 8 0 0 1 5 15zm11.7 0H19a8 8 0 0 1-4.4 4.3 12 12 0 0 0 2.1-4.3z"/></svg>
        <span>www.harrowgatelegal.com.au</span>
      </li>
    </ul>
  </div>
</section>

</body>
</html>
```